Harborstone Lending Business Card Design

We are looking for a nice looking business card design. I'd prefer something other than white for the background but white is ok if necessary. I'm uploading two versions of my picture, one is square and one is rounded. Also a couple of versions of the logo for white backgrounds as well as one for darker backgrounds.

Target Market(s)

Realtors and prospective clients

Industry/Entity Type

Mortgage

Contact Information for Business Card

Double sided business card. Not sure what is needed here.

Colors

Designer to choose colors to be used in the design.

Requirements
Must have
• Name: Marcus Pellham
• Title: Senior Mortgage Advisor
• Email: marcuspellham@harborstonelending.example
• website: www.marcuspellhamhomeloangroup.example
• Address: 4670 W 2850 N, STE 215 Salt Lake City, UT 84192
• Phone: 801-555-0187
• nmls# 948217
• Logo is on our webstie. www.harborstonelending.example
• Picture
Nice to have
• Colors could be similar to our website www.harborstonelending.example
• A list of what we do (VA Loans, FHA Loans, Conventional Loans, USDA Loans)

```html
<!DOCTYPE html>
<html lang="en">
<head>
<meta charset="utf-8">
<title>Harborstone Lending – Business Card</title>
<link rel="stylesheet" href="https://fonts.googleapis.com/css2?family=Exo+2:wght@300;400;600;700&display=swap">
<style>
  :root {
    --backdrop: #353535;
    --paper: #ffffff;
    --ink: #111111;
    --muted: #333333;
    --green: #7fb23a;
    --green-dark: #6b9c2c;
    --silver: #c9cbcd;
    --silver-light: #eceeef;
    --back-text: #a9acae;
    --rule: #444444;
  }
  * { box-sizing: border-box; margin: 0; padding: 0; }
  html, body { width: 1200px; height: 1200px; overflow: hidden; }
  body {
    background: var(--backdrop);
    font-family: "Exo 2", sans-serif;
    position: relative;
  }
  .card {
    position: absolute;
    left: 160px;
    width: 880px;
    height: 503px;
    overflow: hidden;
    box-shadow: 0 10px 30px rgba(0,0,0,.45);
  }
  .card--front { top: 70px; background: var(--paper); color: var(--ink); }
  .card--back { top: 627px; background: var(--ink); }
  .card__bands { position: absolute; inset: 0; width: 880px; height: 503px; }

  .photo {
    position: absolute; left: 70px; top: 36px;
    width: 176px; height: 216px;
    border: 3px solid var(--ink);
    padding: 6px;
    background: var(--paper);
  }
  .photo__fill {
    width: 100%; height: 100%;
    outline: 2px solid var(--ink);
    background: linear-gradient(160deg, #a86a2e 0%, #6b4a2a 40%, #2d2f33 75%, #3d4a57 100%);
  }
  .brand {
    position: absolute; left: 285px; top: 92px;
    display: flex; align-items: center; gap: 14px;
  }
  .brand__mark { width: 34px; height: 34px; background: var(--ink); }
  .brand__name {
    font-weight: 700; font-size: 33px; letter-spacing: 3px;
    text-transform: uppercase; color: var(--ink);
  }
  .card--back .brand__mark { background: var(--silver); }
  .card--back .brand__name { color: var(--silver); }
  .nmls {
    position: absolute; right: 60px; top: 150px;
    font-size: 17px; font-weight: 300; color: var(--muted);
  }
  .person { position: absolute; left: 285px; top: 176px; }
  .person__name {
    font-size: 36px; font-weight: 300; color: var(--green);
    text-transform: uppercase; line-height: 1;
  }
  .person__title { font-size: 19px; font-weight: 400; color: var(--muted); margin-top: 6px; }
  .rule { position: absolute; height: 1px; background: var(--rule); }
  .rule--top { left: 60px; right: 60px; top: 268px; }
  .rule--address { left: 470px; right: 40px; top: 372px; }
  .contact { position: absolute; left: 68px; top: 284px; list-style: none; }
  .contact__item {
    display: flex; align-items: center; gap: 9px;
    font-size: 16px; font-weight: 400; line-height: 27px; color: var(--ink);
  }
  .contact__icon { width: 14px; height: 14px; flex: none; }
  .divider { position: absolute; left: 448px; top: 290px; width: 1px; height: 66px; background: var(--rule); }
  .address {
    position: absolute; left: 470px; top: 296px;
    font-size: 18px; font-weight: 400; line-height: 27px; color: var(--ink);
    display: flex; gap: 9px;
  }
  .address__icon { width: 14px; height: 18px; margin-top: 4px; flex: none; }

  .card--back .brand {
    left: 0; right: 0; top: 170px; justify-content: center;
  }
  .services {
    position: absolute; left: 0; right: 0; top: 232px;
    text-align: center; font-size: 20px; font-weight: 300;
    letter-spacing: 1.5px; line-height: 30px; color: var(--back-text);
  }
</style>
</head>
<body>

<section class="card card--front" aria-label="Business card front">
  <svg class="card__bands" viewBox="0 0 880 503" aria-hidden="true">
    <polygon points="0,402 470,402 512,452 0,452" fill="#111111"/>
    <polygon points="0,452 512,452 520,462 0,462" fill="#d9d9d9"/>
    <polygon points="500,430 880,430 880,503 560,503" fill="#7fb23a"/>
  </svg>

  <div class="photo"><div class="photo__fill" role="img" aria-label="Portrait photo of Marcus Pellham"></div></div>

  <div class="brand"><span class="brand__mark"></span><span class="brand__name">Harborstone Lending</span></div>
  <p class="nmls">nmls 948217</p>

  <div class="person">
    <h1 class="person__name">Marcus Pellham</h1>
    <p class="person__title">Senior Mortgage Advisor</p>
  </div>

  <div class="rule rule--top"></div>

  <ul class="contact">
    <li class="contact__item">
      <svg class="contact__icon" viewBox="0 0 24 24"><path fill="#7fb23a" d="M6.6 10.8a15 15 0 0 0 6.6 6.6l2.2-2.2c.3-.3.7-.4 1-.2 1.1.4 2.3.6 3.6.6.6 0 1 .4 1 1V20c0 .6-.4 1-1 1A17 17 0 0 1 3 4c0-.6.4-1 1-1h3.5c.6 0 1 .4 1 1 0 1.3.2 2.5.6 3.6.1.3 0 .7-.2 1z"/></svg>
      801-555-0187
    </li>
    <li class="contact__item">
      <svg class="contact__icon" viewBox="0 0 24 24"><rect x="2" y="5" width="20" height="14" fill="#7fb23a"/></svg>
      marcuspellham@harborstonelending.example
    </li>
    <li class="contact__item">
      <svg class="contact__icon" viewBox="0 0 24 24"><circle cx="12" cy="12" r="10" fill="#7fb23a"/><path d="M2 12h20M12 2c3 3 3 17 0 20M12 2c-3 3-3 17 0 20" stroke="#fff" stroke-width="1.4" fill="none"/></svg>
      www.marcuspellhamhomeloangroup.example
    </li>
  </ul>

  <div class="divider"></div>

  <address class="address">
    <svg class="address__icon" viewBox="0 0 24 30"><path fill="#7fb23a" d="M12 0a11 11 0 0 0-11 11c0 8 11 19 11 19s11-11 11-19A11 11 0 0 0 12 0zm0 15a4 4 0 1 1 0-8 4 4 0 0 1 0 8z"/></svg>
    <span>4670 W 2850 N<br>STE 215 Salt Lake City, UT 84192</span>
  </address>

  <div class="rule rule--address"></div>
</section>

<section class="card card--back" aria-label="Business card back">
  <svg class="card__bands" viewBox="0 0 880 503" aria-hidden="true">
    <defs>
      <linearGradient id="silverBand" x1="0" y1="0" x2="1" y2="0">
        <stop offset="0" stop-color="#eceeef"/>
        <stop offset="1" stop-color="#9fa2a5"/>
      </linearGradient>
    </defs>
    <polygon points="0,360 420,360 462,412 0,412" fill="url(#silverBand)"/>
    <polygon points="0,372 420,372 438,394 0,394" fill="#111111"/>
    <polygon points="450,410 880,410 880,503 520,503" fill="#7fb23a"/>
  </svg>

  <div class="brand"><span class="brand__mark"></span><span class="brand__name">Harborstone Lending</span></div>

  <p class="services">VA Loans, FHA Loans<br>Conventional Loans, USDA Loans</p>
</section>

</body>
</html>
```